Business Card - Professional Minimalist - Double sided

We appreciate minimalist logo/web/collateral designs that allow design to tell a story. We want to relay a professional image/approach but throwing in a splash of modern when we’re able so long as it’s not distracting. Think 75% classic corporate, 25% modern. Open to black or white design, not sure which might look the best.

Target Market(s)

Senior executives or related government affairs contacts within the agriculture, energy, and defense industries (i.e., potential clients) but located outside of Washington, DC. Most potential clients based in DC with be familiar with both of us and our shared history.

Industry/Entity Type

Consulting

Contact Information for Business Card

Name: Daniel R. Whitlock
Title: Co-Founder & Partner
Address: 418 Bramblewood Ave. SE | Suite 2716 | Washington, D.C. 20019
Phone: (202) 555-0187
Email: Daniel@HollerbyWhitlock.com

Font styles to use
Serif

Colors

Designer to choose only greyscale colors for use in the design.

Requirements
Must have
• Name: Daniel R. Whitlock
Phone: (202) 555-0187

```html
<!DOCTYPE html>
<html lang="en">
<head>
<meta charset="utf-8">
<title>Hollerby Whitlock Group – Business Card</title>
<link rel="stylesheet" href="https://fonts.googleapis.com/css2?family=Noticia+Text:wght@400;700&display=swap">
<style>
  :root {
    --charcoal: #333333;
    --ink: #3a3a3a;
    --paper: #ffffff;
    --accent: #00f0ff;
  }
  * { margin: 0; padding: 0; box-sizing: border-box; }
  html, body {
    width: 1200px;
    height: 779px;
    overflow: hidden;
    background: var(--paper);
  }
  .card {
    position: relative;
    width: 1200px;
    height: 779px;
    background: var(--paper);
    font-family: "Noticia Text", Georgia, serif;
    color: var(--ink);
  }
  .top-band {
    position: absolute;
    left: 0;
    top: 0;
    width: 1200px;
    height: 372px;
    background: var(--charcoal);
  }
  .brand-tab {
    position: absolute;
    left: 547px;
    top: 279px;
    width: 653px;
    height: 93px;
    background: var(--paper);
  }
  .brand-square {
    position: absolute;
    left: 556px;
    top: 288px;
    width: 76px;
    height: 76px;
    background: var(--charcoal);
  }
  .brand-name {
    position: absolute;
    left: 652px;
    top: 292px;
    width: 460px;
    color: var(--charcoal);
    font-weight: 400;
    text-transform: uppercase;
    line-height: 1;
  }
  .brand-name .line-main {
    display: block;
    font-size: 35px;
    letter-spacing: 1px;
    white-space: nowrap;
  }
  .brand-name .line-sub {
    display: block;
    margin-top: 8px;
    font-size: 20px;
    letter-spacing: 9px;
    text-align: right;
  }
  .contact {
    position: absolute;
    left: 92px;
    top: 420px;
  }
  .contact-name {
    font-size: 39px;
    font-weight: 700;
    color: var(--accent);
    line-height: 1.1;
  }
  .contact-title {
    margin-top: 6px;
    font-size: 35px;
    font-weight: 400;
    color: var(--ink);
    line-height: 1.15;
  }
  .contact-details {
    margin-top: 26px;
    font-size: 33px;
    line-height: 52px;
    color: var(--ink);
    font-style: normal;
    white-space: nowrap;
  }
</style>
</head>
<body>
  <div class="card">
    <div class="top-band"></div>
    <div class="brand-tab"></div>
    <div class="brand-square"></div>
    <div class="brand-name">
      <span class="line-main">Hollerby Whitlock</span>
      <span class="line-sub">Group</span>
    </div>

    <div class="contact">
      <h1 class="contact-name">Daniel R. Whitlock</h1>
      <p class="contact-title">Co-Founder &amp; Partner</p>
      <address class="contact-details">
        418 Bramblewood Ave. SE | Suite 2716 | Washington, D.C. 20019<br>
        (202) 555-0187<br>
        Daniel@HollerbyWhitlock.com
      </address>
    </div>
  </div>
</body>
</html>
```